" Consultório médico focado em atendimentos particulares para rinoplastia (principal) e otoplastia - cirurgias estéticas da face . Proposta mais luxuosa, consultório para atendimento mais personalizado focado em estética. "

```html
<!DOCTYPE html>
<html lang="pt-BR">
<head>
<meta charset="utf-8">
<title>Dra. Clara Moreira – Papelaria</title>
<link rel="stylesheet" href="https://fonts.googleapis.com/css2?family=Raleway:wght@300;400;500&family=Montserrat:wght@400;500&display=swap">
<style>
  :root{
    --bg:#8c8c8c;
    --paper:#ffffff;
    --rose:#b9787a;
    --rose-light:#e0aeae;
    --rose-dark:#8e5456;
    --ink:#6d6d6d;
    --ink-soft:#9a9a9a;
  }
  *{margin:0;padding:0;box-sizing:border-box}
  html,body{width:1200px;height:1200px;overflow:hidden}
  body{background:var(--bg);position:relative;font-family:"Raleway",sans-serif}

  .letterhead{position:absolute;left:96px;top:226px;width:461px;height:703px;background:var(--paper)}
  .letterhead__mark{position:absolute;left:200px;top:260px;width:150px;height:150px}
  .letterhead__footer{position:absolute;left:0;right:0;bottom:40px;display:flex;justify-content:space-between;align-items:flex-start;padding:0 26px;font-family:"Montserrat",sans-serif;font-size:7px;line-height:1.45;color:var(--ink-soft)}
  .contact{display:flex;gap:6px;align-items:flex-start}
  .contact svg{width:11px;height:11px;flex:none;fill:var(--rose)}

  .envelope{position:absolute;left:643px;top:204px;width:461px;height:720px;background:var(--paper)}
  .envelope__flap{position:absolute;left:0;top:0;width:461px;height:160px}
  .envelope__band{position:absolute;left:0;right:0;bottom:14px;height:14px;background:linear-gradient(180deg,var(--rose-light),var(--rose) 55%,var(--rose-dark))}
  .brand{position:absolute;left:0;right:0;top:330px;text-align:center}
  .brand__name{display:inline-flex;align-items:center;gap:10px;font-family:"Raleway",sans-serif;font-weight:300;font-size:40px;color:var(--ink);letter-spacing:.5px}
  .brand__dot{width:12px;height:12px;border-radius:50%;background:var(--rose)}
  .brand__tagline{margin-top:6px;font-family:"Montserrat",sans-serif;font-weight:500;font-size:11.5px;letter-spacing:1.6px;color:var(--rose)}
</style>
</head>
<body>

<section class="letterhead" aria-label="Papel timbrado">
  <svg class="letterhead__mark" viewBox="0 0 150 150" aria-hidden="true">
    <circle cx="75" cy="75" r="70" fill="none" stroke="var(--rose-light)" stroke-width="1.5" opacity=".6"/>
  </svg>

  <footer class="letterhead__footer">
    <div class="contact">
      <svg viewBox="0 0 24 24"><path d="M6.6 10.8a15 15 0 0 0 6.6 6.6l2.2-2.2a1 1 0 0 1 1-.25 11.4 11.4 0 0 0 3.6.57 1 1 0 0 1 1 1V20a1 1 0 0 1-1 1A17 17 0 0 1 3 4a1 1 0 0 1 1-1h3.5a1 1 0 0 1 1 1c0 1.25.2 2.45.57 3.57a1 1 0 0 1-.25 1z"/></svg>
      <span>11 98765 4321</span>
    </div>
    <div class="contact">
      <svg viewBox="0 0 24 24"><path d="M3 5h18v14H3zm2 2v.5l7 4.5 7-4.5V7zm0 2.9V17h14V9.9l-7 4.5z"/></svg>
      <span>claramoreira.clinica@email.com<br>@claramoreira.rino</span>
    </div>
    <div class="contact">
      <svg viewBox="0 0 24 24"><path d="M12 2a7 7 0 0 0-7 7c0 5 7 13 7 13s7-8 7-13a7 7 0 0 0-7-7zm0 9.5A2.5 2.5 0 1 1 12 6.5a2.5 2.5 0 0 1 0 5z"/></svg>
      <span>Edifício Solar Sala 412<br>Rua das Acácias, 120<br>Jd Primavera – SP</span>
    </div>
  </footer>
</section>

<section class="envelope" aria-label="Envelope">
  <svg class="envelope__flap" viewBox="0 0 461 160" preserveAspectRatio="none" aria-hidden="true">
    <defs>
      <linearGradient id="flapRose" x1="0" y1="0" x2="1" y2="0">
        <stop offset="0" stop-color="var(--rose-dark)"/>
        <stop offset=".45" stop-color="var(--rose-light)"/>
        <stop offset="1" stop-color="var(--rose)"/>
      </linearGradient>
    </defs>
    <path d="M0 0H461V98Q300 104 60 150L0 112Z" fill="url(#flapRose)"/>
  </svg>

  <div class="brand">
    <div class="brand__name"><span class="brand__dot"></span>Dra. Clara Moreira</div>
    <div class="brand__tagline">OTORRINOLARINGOLOGISTA | RINOPLASTIA</div>
  </div>

  <div class="envelope__band"></div>
</section>

</body>
</html>
```